Business card design needed

I run a Beautician studio (for 7 years now)
I offer
- Velmo Skin Glide
- Lumora Renew
- Nails
- Facials
- Manicure
- Foot Treatment
It might not be necessary to list all those treatments?
Maybe the link to the Website is sufficient?
I leave that up to you ...
(more info on www.BrowsAndBloomByMirela.com.au)
Velmo SkinGlide is our biggest success, It replaces waxing.
I would like to incorporate the logo into the Business Card.
We had many complaints regarding our old Business Cards as the Phone Number was to small.
On the backside, we would like a "your next Appointment" section.
Looking forward to you Design, cheers ... Mirela
Brows by Bloom by Mirela
14 Korrin Pde 3954 Carrowin
www.BrowsAndBloomByMirela.com.au
03 8142 6639

```html
<!DOCTYPE html>
<html lang="en">
<head>
<meta charset="utf-8">
<title>Brows &amp; Bloom by Mirela — Business Card</title>
<link rel="stylesheet" href="https://fonts.googleapis.com/css2?family=Open+Sans:wght@400;700&display=swap">
<style>
  :root {
    --ink: #3d3d3d;
    --paper: #ffffff;
    --night: #0b0b0b;
    --silver: #9b9b9b;
    --sun: #f2a321;
  }
  * { margin: 0; padding: 0; box-sizing: border-box; }
  html, body {
    width: 1200px; height: 693px; overflow: hidden;
    background: var(--paper);
  }
  .card {
    position: relative; width: 1200px; height: 693px;
    background: var(--paper); overflow: hidden;
    font-family: "Open Sans", Arial, sans-serif; color: var(--ink);
  }
  .card__waves { position: absolute; inset: 0; width: 100%; height: 100%; }
  .studio-name {
    position: absolute; left: 76px; top: 76px;
    font-size: 68px; font-weight: 700; letter-spacing: 2px;
    text-transform: uppercase; line-height: 1; white-space: nowrap;
  }
  .studio-web {
    position: absolute; left: 78px; top: 174px;
    font-size: 34px; font-weight: 400; letter-spacing: 8.2px;
    line-height: 1; white-space: nowrap;
  }
  .contact {
    position: absolute; left: 76px; display: flex; align-items: center;
    white-space: nowrap; line-height: 1;
  }
  .contact--phone { top: 358px; font-size: 44px; gap: 14px; }
  .contact--address { top: 442px; font-size: 31px; gap: 16px; }
  .contact__icon { flex: none; }
  .partner {
    position: absolute; left: 852px; top: 436px; width: 282px;
    display: flex; flex-direction: column; align-items: center; gap: 20px;
  }
  .partner__dot {
    width: 118px; height: 118px; border-radius: 50%; background: var(--sun);
  }
  .partner__name {
    color: var(--paper); font-size: 31px; font-weight: 400;
    letter-spacing: 1px; line-height: 1; white-space: nowrap;
  }
</style>
</head>
<body>
<main class="card">
  <svg class="card__waves" viewBox="0 0 1063 614" preserveAspectRatio="none" aria-hidden="true">
    <defs>
      <linearGradient id="swoosh-shade" x1="0" y1="0" x2="1" y2="0">
        <stop offset="0" stop-color="#3a3a3a"/>
        <stop offset="0.5" stop-color="#6e6e6e"/>
        <stop offset="1" stop-color="#bdbdbd"/>
      </linearGradient>
    </defs>
    <path fill="var(--silver)"
      d="M1063,292 C930,296 820,340 700,400 C570,465 420,520 230,522 C180,522 130,518 100,512
         C160,530 220,538 300,538 C470,538 600,490 720,430 C840,372 950,330 1063,318 Z"/>
    <path fill="var(--night)"
      d="M1063,322 C950,332 850,372 730,432 C620,488 500,540 400,568 C350,584 310,600 290,614 L1063,614 Z"/>
    <path fill="url(#swoosh-shade)"
      d="M0,466 C90,505 220,548 380,552 C470,554 550,540 610,518
         C550,552 470,574 370,578 C220,582 100,548 0,510 Z"/>
  </svg>

  <h1 class="studio-name">Brows &amp; Bloom by Mirela</h1>
  <p class="studio-web">www.BrowsAndBloomByMirela.com.au</p>

  <p class="contact contact--phone">
    <svg class="contact__icon" width="38" height="38" viewBox="0 0 38 38" aria-hidden="true">
      <circle cx="19" cy="19" r="17" fill="none" stroke="var(--ink)" stroke-width="2.4"/>
      <path fill="var(--ink)" d="M14,9 C11,11 10,15 11.5,20 C13,25 16.5,28.5 21,29.5 L23.5,26 L20,23.5 L18,25 C16,23.5 14.8,21 14.3,18 L16.6,17 L15.8,12.5 Z"/>
    </svg>
    <span>03 8142 6639</span>
  </p>

  <p class="contact contact--address">
    <svg class="contact__icon" width="28" height="30" viewBox="0 0 28 30" aria-hidden="true">
      <path fill="var(--ink)" d="M14,1 C7,1 2,6 2,12.5 C2,20 14,29 14,29 C14,29 26,20 26,12.5 C26,6 21,1 14,1 Z"/>
      <circle cx="14" cy="12.5" r="4.5" fill="var(--paper)"/>
    </svg>
    <span>14 Korrin Pde 3954 Carrowin</span>
  </p>

  <div class="partner">
    <span class="partner__dot"></span>
    <span class="partner__name">Velmo Skin Glide</span>
  </div>
</main>
</body>
</html>
```